New business card for QT4 Linkway, a marketing company.

We need a new business card design. We would like it to be blue gray and white. We would like some movement but in a more subtle pattern than in the file we uploaded. We are a marketing company that connects brands with their target audiences - we make connections. We work in the New York Metro area with sophisticated clients. The card should feel modern, upscale and professional.

Target Market(s)

Businesses looking to grow their brands in tourism and nightlife. We work with liquor and beer companies and with Tourism bureaus and companies.

Industry/Entity Type

Marketing

Contact Information for Business Card

Would like a horizontal layout, two-sided. Would like the logo on the back with the tagline ' "connecting brands to their target audiences" under the logo. On the front, we would like name, title, contact email, contact phone, website.

Font styles to use
Sans Serif

Colors
3377b5
85cae6
ffffff

Requirements
Must have
• Our logo. See attached. Otherwise, open to your ideas.
Should not have
• No colors we don't want - no reds/pinks/oranges please

```html
<!DOCTYPE html>
<html lang="en">
<head>
<meta charset="utf-8">
<title>QT4 Linkway – Business Card</title>
<link href="https://fonts.googleapis.com/css2?family=Roboto:wght@400;500&family=Roboto+Condensed:wght@400;700&display=swap" rel="stylesheet">
<style>
  :root {
    --backdrop: #262626;
    --card-front: #f7f9fb;
    --brand-blue: #3377b5;
    --brand-blue-deep: #2a6399;
    --brand-sky: #85cae6;
    --title-slate: #7f9bb3;
    --text-slate: #4a5661;
    --icon-slate: #5f7a92;
    --rule-sky: #b9dcee;
    --white: #ffffff;
  }
  * { margin: 0; padding: 0; box-sizing: border-box; }
  html, body {
    width: 1200px; height: 960px; overflow: hidden;
    background: var(--backdrop);
    font-family: "Roboto", Arial, sans-serif;
  }
  .stage { position: relative; width: 1200px; height: 960px; }

  .card { position: absolute; width: 600px; height: 330px; border-radius: 18px; overflow: hidden; }

  /* Front */
  .card-front { left: 314px; top: 113px; background: var(--card-front); }
  .front-brand {
    position: absolute; left: 66px; top: 122px;
    display: flex; align-items: center; gap: 9px;
  }
  .front-brand .brand-dot {
    width: 96px; height: 96px; border-radius: 50%; background: var(--brand-blue); flex: none;
  }
  .front-brand .brand-name {
    font-size: 19px; font-weight: 400; color: var(--brand-blue);
    text-transform: uppercase; white-space: nowrap;
  }
  .divider {
    position: absolute; left: 314px; top: 77px; width: 1px; height: 195px;
    background: var(--rule-sky);
  }
  .contact { position: absolute; left: 343px; top: 76px; }
  .contact .person-name {
    font-family: "Roboto Condensed", Arial, sans-serif;
    font-weight: 700; font-size: 23px; color: var(--brand-blue); line-height: 26px;
  }
  .contact .person-title {
    font-family: "Roboto Condensed", Arial, sans-serif;
    font-size: 15px; color: var(--title-slate); line-height: 18px; letter-spacing: 0.3px;
  }
  .contact .address {
    margin-top: 7px; font-size: 14.5px; color: var(--text-slate); line-height: 18px;
  }
  .contact .lines { margin-top: 7px; list-style: none; }
  .contact .lines li {
    display: flex; align-items: center; gap: 8px;
    font-size: 14.5px; color: var(--text-slate); height: 19px;
  }
  .contact .lines svg { width: 14px; height: 14px; fill: var(--icon-slate); flex: none; }

  /* Back */
  .card-back {
    left: 311px; top: 472px; height: 342px;
    background: linear-gradient(to bottom, var(--brand-blue), var(--brand-blue-deep));
  }
  .back-brand {
    position: absolute; left: 0; right: 0; top: 60px;
    display: flex; flex-direction: column; align-items: center; gap: 18px;
  }
  .back-brand .brand-dot {
    width: 150px; height: 150px; border-radius: 50%; background: var(--brand-sky);
  }
  .back-brand .brand-name {
    font-size: 30px; font-weight: 500; color: var(--white); letter-spacing: 1px;
  }
  .tagline {
    position: absolute; left: 0; right: 0; top: 288px; text-align: center;
    font-size: 15px; color: var(--white);
  }
</style>
</head>
<body>
<main class="stage">

  <section class="card card-front" aria-label="Card front">
    <div class="front-brand">
      <span class="brand-dot"></span>
      <span class="brand-name">QT4 Linkway</span>
    </div>
    <div class="divider"></div>
    <div class="contact">
      <p class="person-name">MARK ELLISON</p>
      <p class="person-title">CEO/FOUNDER</p>
      <p class="address">4120 Harbor View Road<br>Hoboken, New Jersey 07030</p>
      <ul class="lines">
        <li><svg viewBox="0 0 16 16" aria-hidden="true"><path d="M3.6 1.5l2.3 2.8-1.4 1.6c.9 2 2.5 3.6 4.6 4.6l1.6-1.4 2.8 2.3-1.3 2.1C7 13.2 2.8 9 2.5 2.8z"/></svg>201 555 0148</li>
        <li><svg viewBox="0 0 16 16" aria-hidden="true"><path d="M4.5 1h7v14h-7zM6 2.5v9.5h4V2.5zM7.4 13h1.2v1H7.4z" fill-rule="evenodd"/></svg>201 555 0172</li>
        <li><svg viewBox="0 0 16 16" aria-hidden="true"><path d="M4 2h8v3H4zM1.5 6h13v6H12v2.5H4V12H1.5zM5.5 10v3h5v-3z" fill-rule="evenodd"/></svg>201 555 0196</li>
        <li><svg viewBox="0 0 16 16" aria-hidden="true"><path d="M1.5 3.5h13v9h-13zM2.5 4.5L8 8.8l5.5-4.3z" fill-rule="evenodd"/></svg>mark@qt4linkway.com</li>
        <li><svg viewBox="0 0 16 16" aria-hidden="true"><path d="M8 1.5a6.5 6.5 0 1 1 0 13 6.5 6.5 0 0 1 0-13zM5 4.5l2 1-1 2 2 1.5-.5 3 2-2 .5-2.5-2-1.5 1-2z" fill-rule="evenodd"/></svg>www.qt4linkway.com</li>
      </ul>
    </div>
  </section>

  <section class="card card-back" aria-label="Card back">
    <div class="back-brand">
      <span class="brand-dot"></span>
      <span class="brand-name">QT4 Linkway</span>
    </div>
    <p class="tagline">connecting brands to their target audiences</p>
  </section>

</main>
</body>
</html>
```